School Design and Build Sales Brochure

I am looking for a 4 page (Be printed as A3 and folded in half) A4 Brochure I have attached a word document with basic layout, wording and some photos I want included in the brochure. The word document is only a very rough rough guide. I am looking for a designer to really put together something unique and eye catching that will work in getting peoples attention when arriving through the post.

I have also attached a zip file with more photos that can be added to the the brochure should your design lend itself to it.

I have attached logo, business card and letterhead to give you an idea of company colours/ identity but don't feel restricted by this. The brochure is stand alone and there to bring in new customers

I have also posted a website contest for the above company and you can have a look at that informationa as well.

Pages 2-3 of Brochure can be treated as A3 to allow more flexibility when laying out those pages.

Good luck and I look forward to seeing the results.

I use www.quillpressworks.co.uk for my printing so templates / standards / formats for prinitng can be found there.
Updates

Dear All,

Further to your comments I have uploaded a .zip file with all photos from the word document.

As for the vector file I don't seem to have it but it was donw by a designer on artfolkhub I have asked them to send me a copy. As soon as I have it I will upload it.

The first design submitted was very poor, but I am sure much better is to follow.

Kind regards,

Dorian

Dear All,

Vector file for the logo has now been uploaded.

Kind regards,

Dorian

Dear All,

I am not really "feeling" any of the brochures submitted to date, I like some of the design ideas but something is not right. I believe this is because my brief is not quite right. You are producing what I asked for but having looked at it again I would like to make the following changes to the brief,

1. I think there is too much writing. I have uploaded a new word document with the only writing I want on the brochure. I think this will allow more space for photos / design.

The writing must appear on the following pages,

1. About Us - On The Front Page
2. Services we Provide -   On the front page or two middle pages
3. Client List :  On the back page.

2. The front page must have photos on. I would say two at minimum.

Thank you for your efforts so far, I look forward to recieving revised designs.
Kind regards,

Dorian

Target Market(s)

Will be sent by mail to schools within London and the South East to be read by Head Teachers, Premises Managers and Business Managers.

Industry/Entity Type

School

Requirements
Must have
• Schools recieve many many brochures and mail shots. Mine needs to stand out grab their attention. I have always heard that yellow is a good colour for attracting attention but you all probably know what works best.

Contact Information must be large-ish and clear on the front page.

Photos in word document must be used somewhere

Logo (Obviously)

Submissions must be of all pages otherwise they will be eliminated.
Should not have
• I don''t want before pictures on the front cover as I think it detracts and looks a but grubby.

```html
<!DOCTYPE html>
<html lang="en">
<head>
<meta charset="utf-8">
<title>Brightform School Design and Build – Brochure</title>
<link rel="stylesheet" href="https://fonts.googleapis.com/css2?family=PT+Sans:ital,wght@0,400;0,700;1,400;1,700&family=Kalam:wght@400&display=swap">
<style>
:root{
  --yellow:#fff200;
  --orange:#f58220;
  --red:#ed1c24;
  --green:#3aa34a;
  --ink:#231f20;
  --white:#ffffff;
  --faint:#e6d800;
}
*{box-sizing:border-box;margin:0;padding:0}
html,body{width:1200px;height:1079px;overflow:hidden;background:#ffffff}
body{position:relative;font-family:"PT Sans",Arial,sans-serif;color:var(--ink)}
.brochure{position:absolute;left:224px;top:2px;width:1275px;height:1820px;transform:scale(.59);transform-origin:0 0}
.spread{position:absolute;left:0;width:1275px;height:900px;overflow:hidden}
.spread--outer{top:0}
.spread--inner{top:920px}
.spread svg.bg{position:absolute;left:0;top:0}
.abs{position:absolute}
.photo{position:absolute;background:linear-gradient(160deg,#c9d3dc,#8a9aa8)}
.photo--garden{background:linear-gradient(180deg,#8fb4e0 0%,#dfe7ee 35%,#a8653a 55%,#6e8f3a 80%,#4f6b2a 100%)}
.photo--wash{background:linear-gradient(180deg,#e8ecef 0%,#cfd6da 55%,#3c4a7a 100%)}
.photo--blue{background:linear-gradient(160deg,#2f7fc1,#1c5a99)}
.photo--room{background:linear-gradient(180deg,#f1f2ee,#d8d5c8 70%,#4e5a8a)}
.photo--warm{background:linear-gradient(180deg,#f5e6b3,#e8d28a 60%,#b5512b)}
.photo--teal{background:linear-gradient(160deg,#2bb3a3,#e9eef0 60%,#34407a)}
.photo--court{background:linear-gradient(180deg,#9cb6d0 0%,#b75b3a 40%,#2d2f36 70%,#e58a2a 100%)}
.grid-lines{position:absolute}
.brand{position:absolute;background:var(--white);border:5px solid var(--orange);border-radius:48px 0 0 48px;display:flex;flex-direction:column;justify-content:center;padding-left:22px}
.brand--left{border-radius:0 48px 48px 0;padding-left:64px}
.brand__name{font-weight:700;font-size:36px;color:var(--red);line-height:1}
.brand__tag{font-size:11px;font-style:italic;color:var(--ink);margin-top:4px;padding-left:40px}
.ghost-name{font-weight:700;font-size:48px;color:var(--faint);text-align:center;width:100%}
.ghost-tag{font-size:14px;font-style:italic;color:var(--faint);text-align:center;width:100%}
.contact{position:absolute;left:68px;top:708px;width:525px;text-align:center;font-weight:700;font-size:14.5px;line-height:18px}
.body-text{font-size:12.6px;line-height:15.5px;text-align:justify}
.script{font-family:"Kalam",cursive;color:var(--ink)}
.tab{position:absolute;background:var(--orange);display:flex;align-items:center}
.services{position:absolute;left:69px;top:430px;width:420px;font-size:12.6px;line-height:15.5px}
.services h3{font-size:12.6px;font-weight:700;font-style:italic;margin-top:15px}
.services h3:first-child{margin-top:0}
.services ul{list-style:none;padding-left:26px}
.services li::before{content:"•";margin-right:8px}
.design-list{list-style:none;padding-left:22px;margin:10px 0 8px;font-weight:700}
.design-list li::before{content:"•";margin-right:9px}
.clients{position:absolute;top:722px;font-weight:700;font-size:12.8px;line-height:15.5px;color:var(--ink);list-style:none}
.clients li::before{content:"•";color:var(--yellow);margin-right:6px}
</style>
</head>
<body>
<main class="brochure">

  <section class="spread spread--outer">
    <svg class="bg" width="1275" height="900" viewBox="0 0 1275 900">
      <rect width="1275" height="900" fill="var(--orange)"/>
      <rect x="0" y="34" width="1275" height="6" fill="var(--yellow)"/>
      <rect x="0" y="48" width="697" height="802" fill="var(--yellow)"/>
      <rect x="890" y="48" width="385" height="802" fill="var(--yellow)"/>
      <rect x="874" y="40" width="4" height="815" fill="var(--yellow)"/>
      <rect x="0" y="855" width="1275" height="6" fill="var(--yellow)"/>
      <rect x="52" y="102" width="545" height="488" fill="var(--orange)"/>
      <rect x="708" y="278" width="507" height="463" fill="var(--orange)"/>
      <rect x="1198" y="290" width="77" height="14" fill="var(--orange)"/>
      <rect x="1034" y="728" width="4" height="40" fill="var(--yellow)"/>
    </svg>

    <div class="photo photo--garden" style="left:68px;top:117px;width:513px;height:461px" role="img" aria-label="Photo of a finished school garden with timber decking, seating and lawn"></div>
    <svg class="grid-lines" style="left:68px;top:117px" width="513" height="461" viewBox="0 0 513 461" aria-hidden="true">
      <g stroke="var(--yellow)" stroke-width="3">
        <line x1="85" y1="0" x2="85" y2="461"/><line x1="171" y1="0" x2="171" y2="461"/>
        <line x1="256" y1="0" x2="256" y2="461"/><line x1="342" y1="0" x2="342" y2="461"/>
        <line x1="428" y1="0" x2="428" y2="461"/>
        <line x1="0" y1="58" x2="513" y2="58"/><line x1="0" y1="115" x2="513" y2="115"/>
        <line x1="0" y1="173" x2="513" y2="173"/><line x1="0" y1="230" x2="513" y2="230"/>
        <line x1="0" y1="288" x2="513" y2="288"/><line x1="0" y1="345" x2="513" y2="345"/>
        <line x1="0" y1="403" x2="513" y2="403"/>
      </g>
      <rect x="1.5" y="1.5" width="510" height="458" fill="none" stroke="var(--yellow)" stroke-width="3"/>
    </svg>

    <div class="abs" style="left:68px;top:615px;width:525px">
      <div class="ghost-name">Brightform</div>
      <div class="ghost-tag">School Design and Build</div>
    </div>
    <div class="contact">
      Larchmont House, Fernbrook Lane, Ashcombe, Surrey, KT21 4QX<br>
      Tel: 0845 210 4436<br>
      Fax: 0845 210 4436<br>
      Email: info@brightform.co.uk<br>
      Web: www.brightform.co.uk
    </div>

    <div class="brand" style="left:1038px;top:104px;width:245px;height:106px">
      <span class="brand__name">Brightform</span>
      <span class="brand__tag">School Design and Build</span>
    </div>

    <div class="photo photo--wash" style="left:721px;top:299px;width:153px;height:101px" role="img" aria-label="Washroom with row of basins and round mirrors"></div>
    <div class="photo photo--wash" style="left:878px;top:299px;width:154px;height:101px" role="img" aria-label="Washroom basins with patterned panels"></div>
    <div class="photo photo--blue" style="left:1036px;top:299px;width:154px;height:101px" role="img" aria-label="Washroom vanity with blue fish panels"></div>
    <div class="photo photo--room" style="left:721px;top:405px;width:153px;height:101px" role="img" aria-label="Accessible hygiene room with steps"></div>
    <div class="photo photo--room" style="left:878px;top:405px;width:154px;height:101px" role="img" aria-label="Sensory room interior"></div>
    <div class="photo photo--room" style="left:1036px;top:405px;width:154px;height:101px" role="img" aria-label="Changing room with yellow bench"></div>
    <div class="photo photo--room" style="left:721px;top:511px;width:153px;height:101px" role="img" aria-label="Empty refurbished room"></div>
    <div class="photo photo--blue" style="left:878px;top:511px;width:154px;height:101px" role="img" aria-label="Blue therapy pool enclosure"></div>
    <div class="photo photo--room" style="left:1036px;top:511px;width:154px;height:101px" role="img" aria-label="Corridor with handrail"></div>
    <div class="photo photo--teal" style="left:721px;top:617px;width:153px;height:101px" role="img" aria-label="Toilet area with teal cubicles and urinals"></div>
    <div class="photo photo--room" style="left:878px;top:617px;width:154px;height:101px" role="img" aria-label="Small washroom with basin"></div>
    <div class="photo photo--warm" style="left:1036px;top:617px;width:154px;height:101px" role="img" aria-label="Accessible toilet with warm yellow walls"></div>
  </section>

  <section class="spread spread--inner">
    <svg class="bg" width="1275" height="900" viewBox="0 0 1275 900">
      <rect width="1275" height="900" fill="var(--orange)"/>
      <rect x="0" y="36" width="1275" height="5" fill="var(--yellow)"/>
      <rect x="0" y="46" width="485" height="808" fill="var(--yellow)"/>
      <rect x="572" y="46" width="703" height="808" fill="var(--yellow)"/>
      <rect x="1135" y="46" width="7" height="154" fill="var(--orange)"/>
      <rect x="1210" y="40" width="4" height="60" fill="var(--yellow)"/>
      <rect x="490" y="41" width="4" height="820" fill="var(--yellow)"/>
      <rect x="0" y="860" width="1275" height="5" fill="var(--yellow)"/>
      <rect x="68" y="256" width="496" height="108" fill="var(--orange)"/>
      <rect x="816" y="200" width="384" height="100" fill="var(--orange)"/>
      <rect x="1124" y="300" width="5" height="40" fill="var(--orange)"/>
      <path d="M660 854 C700 700 830 640 980 622 C1120 604 1240 560 1275 490 L1275 854 Z" fill="var(--red)"/>
      <path d="M667 854 C705 710 835 652 985 634 C1125 616 1245 572 1275 505 L1275 854 Z" fill="var(--green)"/>
      <path d="M675 854 C712 722 840 665 990 647 C1130 629 1250 586 1275 520 L1275 854 Z" fill="var(--orange)"/>
    </svg>

    <div class="brand brand--left" style="left:-6px;top:60px;width:265px;height:84px">
      <span class="brand__name">Brightform</span>
      <span class="brand__tag">School Design and Build</span>
    </div>

    <p class="abs body-text" style="left:67px;top:170px;width:403px">
      <b>Brightform</b> provides construction, design and project managementservices to schools and the wider education sector. As a client you are always our number one priority and will enjoy unrivalled levels of service, integrity and reliability. Our projects are always carried out to the highest quality, at an agreed fixed cost and within the agreed time.
    </p>

    <div class="photo photo--garden" style="left:78px;top:268px;width:137px;height:90px" role="img" aria-label="Timber garden seating area"></div>
    <div class="photo photo--room" style="left:222px;top:268px;width:60px;height:90px" role="img" aria-label="School corridor"></div>
    <div class="photo photo--teal" style="left:289px;top:268px;width:61px;height:90px" role="img" aria-label="Toilet cubicles with pink doors"></div>
    <div class="photo photo--room" style="left:357px;top:268px;width:60px;height:90px" role="img" aria-label="Accessible toilet"></div>
    <div class="photo photo--court" style="left:425px;top:268px;width:134px;height:90px" role="img" aria-label="Playground with trampoline surfacing"></div>

    <div class="tab" style="left:0;top:383px;width:147px;height:30px;padding-left:70px">
      <span class="script" style="font-size:17px">Services :</span>
    </div>

    <div class="services">
      <h3>New Builds and Extensions<br>Refurbishment of all areas including :</h3>
      <ul>
        <li>Receptions</li><li>Toilet Areas</li><li>Classrooms</li><li>Corridors</li>
        <li>Staff Rooms</li><li>Food Technology</li><li>Design Technology</li>
        <li>ICT Suites</li><li>Libraries</li><li>Halls and Sports halls</li>
      </ul>
      <h3>Specialist Special Needs Rooms</h3>
      <ul>
        <li>Changing rooms</li><li>Sensory rooms</li><li>Therapy pools</li>
        <li>Hoist Installations</li><li>Access and DDA Compliance</li>
      </ul>
      <h3>General Buildings Maintenance</h3>
      <h3>Playground Design</h3>
      <h3>Playground Equipment, Surfacing and Bespoke Structures</h3>
      <h3>Temporary Buildings and Classrooms</h3>
    </div>

    <p class="abs body-text" style="left:722px;top:55px;width:398px">
      As a company we are passionate about the environment and our social responsibility. Wherever possible all construction materials are purchased from sustainable sources and our designs encompass many carbon and energy reducing elements as standard. Brightform and and our employees organise many fundraising activities throughout the year the proceeds of which support charities and projects in developing countries. We are an equal opportunities employer that provides a professional environment that is challenging, rewarding, creative and respectful of ideas and individuals.
    </p>

    <div class="photo photo--room" style="left:826px;top:210px;width:118px;height:80px" role="img" aria-label="Changing room with yellow bench"></div>
    <div class="photo photo--teal" style="left:949px;top:210px;width:118px;height:80px" role="img" aria-label="Toilet area with cubicles"></div>
    <div class="photo photo--wash" style="left:1073px;top:210px;width:118px;height:80px" role="img" aria-label="Washroom with basins and mirrors"></div>

    <div class="tab" style="left:642px;top:325px;width:390px;height:33px;padding-left:80px">
      <span class="script" style="font-size:17px">Design and Project Management</span>
    </div>

    <div class="abs body-text" style="left:722px;top:373px;width:480px">
      <p><b>Brightform</b> provides a detailed design service. By working in partnership with the Head Teachers and Team Leaders we are able to capture and interpret your vision for the works required. Design services we can offer include,</p>
      <ul class="design-list">
        <li>Full Planning Permission Applications</li>
        <li>Single / Multiple Room Refurbishments</li>
        <li>Playground Design</li>
        <li>Furniture / Workspace Design and Layout</li>
      </ul>
      <p><b>Brightform</b> offer a dedicated Project Management Service aimed at schools having works carried out by <b>BSF&nbsp; Local Authority contractors.</b> When appointed we represent the school offering Technical, Financial and Project Management support to the Head teacher and Governors ensuring projects are delivered to your specification, within budget and on time</p>
    </div>

    <div class="abs script" style="left:920px;top:662px;font-size:24px">Client list</div>
    <ul class="clients" style="left:722px">
      <li>Ashdown Primary School</li><li>Little Acorns Nursery</li><li>Cedar Market Nursery</li>
      <li>Hillcrest School</li><li>Thomas Wexley Primary</li><li>Meridian School</li>
      <li>Glenmore Primary School</li><li>Elmbrook School</li>
    </ul>
    <ul class="clients" style="left:993px">
      <li>Southmead Primary</li><li>Mill Lane Primary School</li><li>Kingsgate Primary School</li>
      <li>Brookside Primary School</li><li>Borough of Eastmere</li><li>Borough of Westcombe</li>
      <li>Borough of Harlowfield</li><li>Borough of Northbridge</li>
    </ul>
  </section>

</main>
</body>
</html>
```